Film Company needs Poster Design Project for upcoming film "VANE"

At Brindlewood Films, we need a poster design for our upcoming feature film project "VANE," America first 'rock and roll' star. Our film will cover Tobias Merrick Vane's life his drinking, passion and writing. It will not be a horror film, but rather a biopic on his life.
Brindlewood Films is a full service film and television production company, founded by Curtis Belmont and Quarnet, LLC in 2006. Brindlewood Films’ mission is to blend artistic talent with engaging stories to create feature films and television that delight audiences of all ages.
We would like to see designs that embody Tobias Merrick Vane as a person. The film will cover most of his famous poems/novels/short stories so any reference to "Hollow lantern" or "The Quill Moth," etc...would work.
Updates
Thank you ALL for the amazing work you have submitted, you made it really hard for me to come up with one choice. I will make my decision by Wednesday.
Target Market(s)
Target audience 18 - 35
Industry/Entity Type
It Company
Look and feel

```html
<!DOCTYPE html>
<html lang="en">
<head>
<meta charset="utf-8">
<title>Brindlewood Films presents VANE</title>
<link rel="stylesheet" href="https://fonts.googleapis.com/css2?family=Alegreya:ital,wght@0,400;1,400&family=Arimo:wght@400&family=Cinzel:wght@700&family=Marcellus&family=Rye&display=swap">
<style>
  :root {
    --brown-deep: #34200f;
    --brown-mid: #3f2816;
    --gold-frame: #d6a23c;
    --orange: #f2a33a;
    --gold-light: #f7dc7a;
    --gold-dark: #b9861e;
    --cream: #f0d8a6;
    --red: #c6222b;
    --white: #ffffff;
  }
  * { box-sizing: border-box; margin: 0; padding: 0; }
  html, body { width: 873px; height: 1200px; overflow: hidden; background: var(--white); }
  .poster {
    position: relative;
    width: 873px;
    height: 1200px;
    background: var(--brown-mid);
    border: 4px solid var(--white);
    overflow: hidden;
  }
  .damask-field {
    position: absolute;
    inset: 0;
    background: radial-gradient(ellipse at 50% 45%, #442c18 0%, var(--brown-deep) 100%);
  }
  .gold-frame {
    position: absolute;
    left: 31px; top: 31px; right: 31px; bottom: 31px;
    border: 3px solid var(--gold-frame);
  }
  .studio-name {
    position: absolute;
    top: 66px; left: 0; width: 100%;
    text-align: center;
    font-family: "Cinzel", serif;
    font-weight: 700;
    font-size: 50px;
    letter-spacing: 1px;
    line-height: 1.2;
    color: var(--orange);
  }
  .presents {
    position: absolute;
    top: 176px; left: 0; width: 100%;
    text-align: center;
    font-family: "Alegreya", serif;
    font-size: 62px;
    color: var(--orange);
  }
  .flourish {
    position: absolute;
    left: 40px; top: 330px;
    width: 740px; height: 340px;
    border-radius: 50%;
    background: radial-gradient(ellipse at 50% 50%, rgba(240,216,166,0.55) 0%, rgba(216,170,90,0.3) 50%, rgba(216,170,90,0) 75%);
  }
  .title {
    position: absolute;
    left: 0; top: 270px;
    width: 873px; height: 480px;
  }
  .title text {
    font-family: "Rye", serif;
    font-size: 600px;
  }
  .tagline {
    position: absolute;
    top: 783px; left: 0; width: 100%;
    text-align: center;
    font-family: "Alegreya", serif;
    font-style: italic;
    font-size: 40px;
    color: var(--white);
  }
  .release {
    position: absolute;
    top: 882px; left: 0; width: 100%;
    text-align: center;
    font-family: "Marcellus", serif;
    font-size: 72px;
    letter-spacing: 2px;
    color: var(--red);
  }
  .contact {
    position: absolute;
    top: 1030px; left: 0; width: 100%;
    text-align: center;
    font-family: "Arimo", sans-serif;
    color: var(--white);
  }
  .contact-lead { font-size: 27px; line-height: 31px; }
  .contact-url { font-size: 38px; margin-top: 14px; }
</style>
</head>
<body>
  <main class="poster">
    <div class="damask-field" role="img" aria-label="Dark brown damask wallpaper pattern"></div>
    <div class="gold-frame"></div>

    <h2 class="studio-name">Brindlewood Films</h2>
    <p class="presents">Presents</p>

    <div class="flourish" role="img" aria-label="Pale gold baroque scroll flourish behind the title"></div>

    <svg class="title" viewBox="0 0 873 480" aria-labelledby="film-title">
      <defs>
        <linearGradient id="gold-leaf" x1="0" y1="0" x2="1" y2="1">
          <stop offset="0" stop-color="var(--gold-light)"/>
          <stop offset="0.45" stop-color="#e9b93a"/>
          <stop offset="0.7" stop-color="var(--gold-light)"/>
          <stop offset="1" stop-color="var(--gold-dark)"/>
        </linearGradient>
      </defs>
      <text id="film-title" x="118" y="462" textLength="640" lengthAdjust="spacingAndGlyphs"
            fill="url(#gold-leaf)" stroke="#5a3a12" stroke-width="3">VANE</text>
    </svg>

    <p class="tagline">America’s First 'Rock and Roll' Star</p>
    <p class="release">COMING SOON</p>

    <div class="contact">
      <p class="contact-lead">For more information<br>see us at</p>
      <p class="contact-url">www.brindlewoodpictures.com</p>
    </div>
  </main>
</body>
</html>
```